A single page website & logo required for a Field Service Management Application

Name of the project - CrewTallo

We are software developers and we have a Field Service Management application ready. This software is all about optimizing the businesses that send their staff to various sites to provide service. Scheduling, creating jobs, quotes & invoices are a few salient features of it. It also has an accompanying Android & iPhone/iPad versions that will be used by the technicians.

More details can be provided, if needed.

After this web design project ends, the winning designer will be awarded the budget for the logo design through a 1on1 project.

Reason: I need to get the designs approved from my boss and he is currently overseas and is very busy. And hence I need the timeline to be extended.

Target Market(s)

All the Companies all over the world that send their staff to various sites to provide service.

Industry/Entity Type

Software

Logo Text

CrewTallo

Number of Pages Required

1 page

Font styles to use
Serif
Sans Serif

Requirements
Must have
• We would like to have the following components in the design:
• 1. Slider
• 2. Features of the software
• 3. Pricing Details
• 4. FAQs
• 5. Suitable for (Shows a list of all industries that our software is suitable for)
Nice to have
• A section with the background of a technician using our app on a mobile device (Screenshot can be provided)
Should not have
• Gaudy fonts and stereotypical designs

```html
<!DOCTYPE html>
<html lang="en">
<head>
<meta charset="utf-8">
<title>CrewTallo – Field Service Management</title>
<link href="https://fonts.googleapis.com/css2?family=Ubuntu:wght@300;400;500;700&display=swap" rel="stylesheet">
<style>
:root{
  --orange:#ff6a00;
  --orange-light:#ff8f1f;
  --header:#3b3b3b;
  --yellow:#ffd400;
  --text:#2b2b2b;
  --footer:#efefef;
  --white:#ffffff;
}
*{margin:0;padding:0;box-sizing:border-box}
html,body{width:1200px;height:2761px;overflow:hidden}
body{font-family:"Ubuntu",Arial,sans-serif;color:var(--text);background:var(--white);position:relative}
section,header,footer{position:absolute;left:0;width:1200px}
.btn{display:inline-block;font-size:12px;color:var(--white);background:#555;padding:8px 11px;text-decoration:none}

/* header */
.site-header{top:0;height:88px;background:var(--header);z-index:2}
.brand{position:absolute;left:16px;top:30px;font-size:25px;color:var(--white);font-weight:400}
.brand span{color:var(--orange)}
.main-nav{position:absolute;right:30px;top:38px;display:flex;gap:24px;font-size:13px}
.main-nav a{color:var(--white);text-decoration:none}
.main-nav a.active{color:var(--orange)}

/* hero */
.hero{top:88px;height:516px}
.hero-photo{position:absolute;inset:0;background:linear-gradient(100deg,#5b5249 0%,#8d7d6b 35%,#e9e2d0 60%,#6a6761 85%,#3b4350 100%)}
.hero-text{position:absolute;left:170px;top:198px;color:var(--white)}
.hero-text .lead{font-size:26px;color:#111;font-weight:400}
.hero-text h1{font-size:40px;color:var(--orange);font-weight:400;margin-top:4px}
.hero-text .btn{margin-top:16px;background:#444}
.hero-arrow{position:absolute;top:246px}
.hero-arrow.left{left:28px}.hero-arrow.right{right:28px}

/* features */
.features{top:604px;height:406px;background:linear-gradient(100deg,var(--orange) 0%,var(--orange-light) 50%,var(--orange) 100%);color:var(--white)}
.section-title{text-align:center;font-size:28px;font-weight:500;color:var(--white)}
.features .section-title{padding-top:64px}
.feature-list{position:absolute;top:142px;left:28px;display:flex;gap:60px}
.feature{width:330px}
.feature h3{display:flex;align-items:center;gap:14px;font-size:22px;font-weight:400;height:40px}
.feature h3 svg{flex:0 0 auto}
.feature p{font-size:12px;line-height:24px;margin-top:14px;font-weight:300}
.feature .btn{margin-top:14px}

/* pricing */
.pricing{top:1010px;height:494px}
.pricing-photo{position:absolute;inset:0;background:linear-gradient(110deg,#1d1d1d 0%,#3a3532 45%,#2b2623 70%,#181818 100%)}
.pricing .section-title{position:absolute;top:100px;width:100%}
.plans{position:absolute;top:170px;left:31px;display:flex}
.plan{width:376px;height:190px;text-align:center;padding-top:22px;color:var(--white);font-size:28px;line-height:32px}
.plan .name{color:#222}
.plan.basic{background:linear-gradient(120deg,#ff6a00,#ff7f10)}
.plan.pro{background:linear-gradient(120deg,#2f9d34,#3fb545);width:390px}
.plan.business{background:linear-gradient(120deg,#5a36b0,#7a49bd);width:373px}
.plan.business .name{color:#1c1466}
.plan-btn{display:inline-block;margin-top:14px;width:166px;height:46px;line-height:46px;font-size:14px;background:var(--yellow);color:var(--white)}
.plan.pro .plan-btn{background:var(--orange);color:var(--yellow)}

/* faqs */
.faqs{top:1504px;height:414px}
.faq-head{position:absolute;left:28px;right:28px;top:52px;height:48px;border-bottom:1px solid #e3e3e3;display:flex;align-items:center;gap:8px}
.faq-head h2{font-size:28px;font-weight:700;color:#111}
.faq-arrows{position:absolute;right:4px;top:12px}
.faq-list{position:absolute;top:150px;left:28px;display:flex;gap:60px}
.faq{width:330px}
.faq h3{font-size:16px;line-height:23px;color:var(--orange);font-weight:500}
.faq p{font-size:12px;line-height:24px;margin-top:20px;color:var(--text)}

/* app section */
.app{top:1918px;height:564px}
.app-photo{position:absolute;inset:0;background:radial-gradient(ellipse at 35% 45%,#8f9bab 0%,#5e7894 40%,#2f4f72 100%)}
.app-card{position:absolute;left:728px;top:186px;width:354px;height:206px;background:rgba(30,30,30,.9);padding:24px 12px;color:var(--white)}
.app-card h3{font-size:23px;font-weight:400}
.app-card h3 span{color:var(--orange)}
.app-card p{font-size:12px;line-height:23px;margin-top:10px}
.badges{display:flex;gap:6px;margin-top:10px}
.badge{width:97px;height:29px;border-radius:4px}
.badge.one{background:#111;border:1px solid #777}
.badge.two{background:#8bc63f}

/* suitable for */
.suitable{top:2482px;height:162px;text-align:center}
.suitable h2{font-size:15px;letter-spacing:3px;font-weight:500;padding-top:46px;color:#222}
.industries{display:flex;justify-content:center;gap:48px;margin-top:38px;font-size:19px;color:#333}

/* footer */
.site-footer{top:2644px;height:117px;background:var(--footer)}
.footer-nav{position:absolute;left:28px;top:32px;font-size:13px;display:flex}
.footer-nav a{color:#222;text-decoration:none;padding:0 14px;border-left:1px solid #222}
.footer-nav a:first-child{padding-left:0;border-left:none}
.copyright{position:absolute;left:28px;top:68px;font-size:13px;color:#222}
.social{position:absolute;right:106px;top:40px;display:flex;gap:8px}
.social span{width:32px;height:32px;border-radius:4px;display:block}
.social .fb{background:#3b5998}.social .tw{background:#4aa3df}
</style>
</head>
<body>

<header class="site-header">
  <div class="brand"><span>CrewTallo</span> Technologies</div>
  <nav class="main-nav">
    <a class="active" href="#">Home</a><a href="#">About Us</a><a href="#">Services</a><a href="#">Testimonials</a><a href="#">Contact Us</a>
  </nav>
</header>

<section class="hero">
  <div class="hero-photo" role="img" aria-label="Photo of a businesswoman holding a tablet in front of city buildings"></div>
  <svg class="hero-arrow left" width="20" height="36" viewBox="0 0 20 36"><path d="M17 3 3 18l14 15" fill="none" stroke="#fff" stroke-width="4"/></svg>
  <svg class="hero-arrow right" width="20" height="36" viewBox="0 0 20 36"><path d="M3 3l14 15L3 33" fill="none" stroke="#fff" stroke-width="4"/></svg>
  <div class="hero-text">
    <p class="lead">We have a software which is designed for</p>
    <h1>Field Service Management</h1>
    <a class="btn" href="#">Learn More</a>
  </div>
</section>

<section class="features">
  <h2 class="section-title">FEATURES OF THE SOFTWARE</h2>
  <div class="feature-list">
    <div class="feature">
      <h3><svg width="38" height="36" viewBox="0 0 38 36"><rect x="3" y="6" width="24" height="28" fill="none" stroke="#333" stroke-width="3"/><path d="M8 14h14M8 20h14M8 26h9" stroke="#333" stroke-width="2.5"/><path d="M22 24 35 4" stroke="#333" stroke-width="4"/></svg>Quotes &amp; Invoices</h3>
      <p>It has survived not only five centuries, but also the leap into electronic typesetting, remaining essentially unchanged. It was popularised in the 1960s with the release of Inkwell sheets containing</p>
      <a class="btn" href="#">Read More</a>
    </div>
    <div class="feature">
      <h3><svg width="36" height="36" viewBox="0 0 36 36"><circle cx="18" cy="18" r="15" fill="none" stroke="#333" stroke-width="3.5"/><path d="M18 9v10h8" fill="none" stroke="#333" stroke-width="3.5"/></svg>Scheduling</h3>
      <p>It has survived not only five centuries, but also the leap into electronic typesetting, remaining essentially unchanged. It was popularised in the 1960s with the release of Inkwell sheets containing</p>
      <a class="btn" href="#">Read More</a>
    </div>
    <div class="feature">
      <h3><svg width="30" height="36" viewBox="0 0 30 38"><rect x="4" y="6" width="22" height="30" rx="3" fill="#333"/><rect x="9" y="2" width="12" height="8" rx="2" fill="#333"/><rect x="9" y="14" width="12" height="14" fill="#ff7a10"/></svg>Creating Jobs</h3>
      <p>It has survived not only five centuries, but also the leap into electronic typesetting, remaining essentially unchanged. It was popularised in the 1960s with the release of Inkwell sheets containing</p>
      <a class="btn" href="#">Read More</a>
    </div>
  </div>
</section>

<section class="pricing">
  <div class="pricing-photo" role="img" aria-label="Dim photo of people working together at a table"></div>
  <h2 class="section-title">PRICING DETAILS</h2>
  <div class="plans">
    <div class="plan basic"><div class="name">Basic</div>$19<br>per month<br><span class="plan-btn">CLICK ON SIGN UP</span></div>
    <div class="plan pro"><div class="name">Professional</div>$49<br>per month<br><span class="plan-btn">CLICK ON SIGN UP</span></div>
    <div class="plan business"><div class="name">Business</div>$119<br>per month<br><span class="plan-btn">CLICK ON SIGN UP</span></div>
  </div>
</section>

<section class="faqs">
  <div class="faq-head">
    <svg width="32" height="32" viewBox="0 0 32 32"><circle cx="16" cy="16" r="16" fill="#ff6a00"/><path d="M11 12a5 5 0 1 1 7 4.5c-1.5.7-2 1.5-2 3" fill="none" stroke="#fff" stroke-width="3.2"/><circle cx="16" cy="24.5" r="2" fill="#fff"/></svg>
    <h2>FAQS</h2>
    <svg class="faq-arrows" width="18" height="10" viewBox="0 0 18 10"><path d="M6 1 2 5l4 4M12 1l4 4-4 4" fill="none" stroke="#222" stroke-width="2"/></svg>
  </div>
  <div class="faq-list">
    <div class="faq"><h3>Neque porro quisquam est qui dolorem ipsum quia dolor sit amet, consectetur, adipisci velit... ?</h3><p>It has survived not only five centuries, but also the leap into electronic typesetting, remaining essentially unchanged. It was popularised in the 1960s with the release of Inkwell sheets containing</p></div>
    <div class="faq"><h3>Neque porro quisquam est qui dolorem ipsum quia dolor sit amet, consectetur, adipisci velit... ?</h3><p>It has survived not only five centuries, but also the leap into electronic typesetting, remaining essentially unchanged. It was popularised in the 1960s with the release of Inkwell sheets containing</p></div>
    <div class="faq"><h3>Neque porro quisquam est qui dolorem ipsum quia dolor sit amet, consectetur, adipisci velit... ?</h3><p>It has survived not only five centuries, but also the leap into electronic typesetting, remaining essentially unchanged. It was popularised in the 1960s with the release of Inkwell sheets containing</p></div>
  </div>
</section>

<section class="app">
  <div class="app-photo" role="img" aria-label="Photo of a hand holding a smartphone showing the app on a blurred blue background"></div>
  <div class="app-card">
    <h3><span>CrewTallo</span> Technologies</h3>
    <p>It has survived not only five centuries, but also the leap into electronic typesetting, remaining essentially unchanged. It was popularised .</p>
    <div class="badges"><span class="badge one"></span><span class="badge two"></span></div>
  </div>
</section>

<section class="suitable">
  <h2>SUITABLE FOR</h2>
  <div class="industries">
    <span>Harbor City Journal</span><span>Ledgerline</span><span>Civic Wire</span><span>Trade Observer</span><span>TechRally</span><span>Bayside Times</span>
  </div>
</section>

<footer class="site-footer">
  <nav class="footer-nav"><a href="#">Home</a><a href="#">About Us</a><a href="#">Services</a><a href="#">Testimonials</a><a href="#">Contact Us</a></nav>
  <p class="copyright">© 2015 Company Name, All Rights Reserved</p>
  <div class="social"><span class="fb"></span><span class="tw"></span></div>
</footer>

</body>
</html>
```